Business card design for a teacher - double sided, sleek design.

My name is Lina and I am an online Arabic language teacher. I am looking for a beautiful business card design for my online teaching business.

The cards will be printed in 85mm x 55mm size.
The card can be either portrait or landscape.

The design should contain my logo on one side and information on the other.

The design needs to be clean and modern. Use of subtle Arabic geometric patterns would be nice. Icons for the social media information on the card should also match the design theme.

My logo font is Consolas, which is a Monospace font.

Business card design should be delivered with editable PSD or EPS files in the handover.

Thanks

Lina

----

Information on the back:

URL: www.speakwithlina.net [this should stand out more than other details]
Email: info@speakwithlina.net
Instagram: @speakwithlina
Facebook: facebook.com/speakwithlina
Skype: speakwithlina

My brand colours are shown in the logo attached. These are:
- Teal green - 4DC9C1
- Mango yellow - FFD600

Target Market(s)

- Young professionals
- Expatriates
- Women and Men

Industry/Entity Type

Education

Contact Information for Business Card

Information on the back:

Skype: speakwithlina

- Teal green - 4DC9C1
- Mango yellow - FFD600

Font styles to use
Other font styles liked:
• Any font complimentary to my logo font which is a Monospace font called Consolas.

Colors

Designer to choose colors to be used in the design.

Requirements
Must have
• - Aesthetically pleasing look
• - Complimentary design with existing logo
Nice to have
• Arabic geometrical patterns

```html
<!DOCTYPE html>
<html lang="en">
<head>
<meta charset="utf-8">
<title>Speak with Lina – Business Card</title>
<link href="https://fonts.googleapis.com/css2?family=Inconsolata:wght@400;700&display=swap" rel="stylesheet">
<style>
  :root {
    --teal: #4dc9c1;
    --grey: #77787a;
    --ink: #1d1d1f;
    --paper: #fbfbfb;
    --backdrop: #e9e6e1;
  }
  * { margin: 0; padding: 0; box-sizing: border-box; }
  html, body { width: 1200px; height: 892px; overflow: hidden; }
  body {
    background: var(--backdrop);
    font-family: "Inconsolata", monospace;
    color: var(--ink);
    position: relative;
  }
  .card {
    position: absolute;
    top: 271px;
    width: 540px;
    height: 350px;
    background: var(--paper);
    box-shadow: 0 6px 18px rgba(0,0,0,.18);
    overflow: hidden;
  }
  .card--info { left: 40px; }
  .card--logo { left: 620px; }
  .card__wave { position: absolute; inset: 0; width: 100%; height: 100%; }

  .brand {
    position: absolute;
    font-weight: 700;
    color: var(--teal);
    letter-spacing: .04em;
    white-space: nowrap;
  }
  .card--info .brand { right: 48px; top: 48px; font-size: 28px; }
  .card--logo .brand { left: 0; right: 0; text-align: center; top: 118px; font-size: 38px; }

  .contact {
    position: absolute;
    left: 34px;
    top: 150px;
    list-style: none;
    font-size: 17px;
    line-height: 25px;
  }
  .contact__item { display: flex; align-items: center; gap: 9px; }
  .contact__item--web { font-weight: 700; font-size: 18px; }
  .contact__icon {
    width: 16px; height: 16px;
    border-radius: 3px;
    background: var(--teal);
    flex: none;
    display: flex; align-items: center; justify-content: center;
  }
  .contact__icon svg { width: 12px; height: 12px; }

  .card__url {
    position: absolute;
    left: 0; right: 0;
    text-align: center;
    top: 205px;
    font-size: 20px;
    letter-spacing: .02em;
    white-space: nowrap;
  }
</style>
</head>
<body>

  <section class="card card--info" aria-label="Card side with contact details">
    <svg class="card__wave" viewBox="0 0 540 350" preserveAspectRatio="none" aria-hidden="true">
      <path d="M150 350 C260 330 330 250 400 200 C450 165 500 150 540 145 L540 350 Z" fill="var(--grey)"/>
      <path d="M150 350 C260 330 330 250 400 200 C450 165 500 150 540 145" fill="none" stroke="#fff" stroke-width="6"/>
      <path d="M135 350 C250 325 320 240 395 188 C445 155 500 138 540 132" fill="none" stroke="var(--teal)" stroke-width="3"/>
    </svg>

    <p class="brand">Speak with Lina</p>

    <ul class="contact">
      <li class="contact__item"><span class="contact__icon"></span>speakwithlina</li>
      <li class="contact__item"><span class="contact__icon"></span>@speakwithlina</li>
      <li class="contact__item"><span class="contact__icon"></span>facebook.com/speakwithlina</li>
      <li class="contact__item">
        <span class="contact__icon">
          <svg viewBox="0 0 12 12"><rect x="1" y="2.5" width="10" height="7" fill="none" stroke="#fff" stroke-width="1.2"/><path d="M1 2.5 L6 7 L11 2.5" fill="none" stroke="#fff" stroke-width="1.2"/></svg>
        </span>info@speakwithlina.net
      </li>
      <li class="contact__item contact__item--web">
        <span class="contact__icon">
          <svg viewBox="0 0 12 12"><circle cx="6" cy="6" r="4.6" fill="none" stroke="#fff" stroke-width="1.1"/><ellipse cx="6" cy="6" rx="2" ry="4.6" fill="none" stroke="#fff" stroke-width="1"/><line x1="1.4" y1="6" x2="10.6" y2="6" stroke="#fff" stroke-width="1"/></svg>
        </span>www.speakwithlina.net
      </li>
    </ul>
  </section>

  <section class="card card--logo" aria-label="Card side with name">
    <svg class="card__wave" viewBox="0 0 540 350" preserveAspectRatio="none" aria-hidden="true">
      <path d="M0 0 L0 350 L120 350 C60 290 40 200 30 120 C25 70 15 30 0 0 Z" fill="var(--teal)"/>
      <path d="M120 350 C60 290 40 200 30 120 C25 70 15 30 0 0" fill="none" stroke="#fff" stroke-width="6"/>
      <path d="M138 350 C72 290 50 200 40 120 C34 70 22 30 6 0" fill="none" stroke="var(--grey)" stroke-width="4"/>
    </svg>

    <p class="brand">Speak with Lina</p>
    <p class="card__url">www.speakwithlina.net</p>
  </section>

</body>
</html>
```